3" Round Business Card for Funeral Home

We need a business card designed for our cremation service. We would like to use a 3" round business card.

The business card will be 2-sided. One side with the logo featured prominently. The back sad will have employee name and contact info.

Templates for printing have been attached to project as well as logo

We like soft colors like the logo. Final design should promote a feeling of trust.

Industry/Entity Type

Funeral

Contact Information for Business Card

Employee Name, Phone number, email, web address

Requirements
Should not have
• any sort of funeral item such as urn, casket, hearse, tombstone

```html
<!DOCTYPE html>
<html lang="en">
<head>
<meta charset="utf-8">
<title>Round Business Card – GentleRest</title>
<link rel="stylesheet" href="https://fonts.googleapis.com/css2?family=Oswald:wght@500&family=Poppins:wght@400;500&display=swap">
<style>
  :root {
    --backdrop: #9c9c9c;
    --plum: #92278f;
    --teal: #1aa39b;
    --white: #ffffff;
    --card-size: 466px;
  }
  * { margin: 0; padding: 0; box-sizing: border-box; }
  html, body {
    width: 1125px;
    height: 1200px;
    overflow: hidden;
  }
  body {
    background: var(--backdrop);
    position: relative;
    font-family: "Poppins", sans-serif;
  }
  .card {
    position: absolute;
    left: 328px;
    width: var(--card-size);
    height: var(--card-size);
    border-radius: 50%;
    text-align: center;
  }
  .card--contact {
    top: 106px;
    background: var(--plum);
    color: var(--white);
  }
  .card--brand {
    top: 627px;
    background: var(--white);
  }
  .contact__name {
    position: absolute;
    top: 104px;
    width: 100%;
    font-family: "Oswald", sans-serif;
    font-weight: 500;
    font-size: 31px;
    letter-spacing: 0.5px;
    color: var(--teal);
    line-height: 1;
  }
  .contact__title {
    position: absolute;
    top: 142px;
    width: 100%;
    font-weight: 500;
    font-size: 18px;
    line-height: 1.2;
  }
  .contact__address {
    position: absolute;
    top: 188px;
    width: 100%;
    font-size: 18.5px;
    line-height: 23px;
  }
  .contact__divider {
    position: absolute;
    top: 251px;
    left: 114px;
    width: 224px;
    height: 24px;
    display: flex;
    align-items: center;
    gap: 6px;
  }
  .contact__rule {
    flex: 1;
    height: 1px;
    background: var(--teal);
  }
  .contact__icon {
    width: 24px;
    height: 24px;
    border-radius: 50%;
    background: var(--teal);
    display: flex;
    align-items: center;
    justify-content: center;
  }
  .contact__icons { display: flex; gap: 5px; margin: 0 4px; }
  .contact__details {
    position: absolute;
    top: 287px;
    width: 100%;
    font-size: 18.5px;
    line-height: 24px;
  }
  .brand__name {
    position: absolute;
    top: 193px;
    width: 100%;
    font-size: 52px;
    font-weight: 400;
    color: var(--teal);
    line-height: 1;
    letter-spacing: -0.5px;
  }
</style>
</head>
<body>
  <section class="card card--contact">
    <h1 class="contact__name">DANIEL FOSTER</h1>
    <p class="contact__title">Founder &amp; CEO</p>
    <p class="contact__address">4210 Willow Bend Road<br>Fairview, Oregon 97024</p>
    <div class="contact__divider">
      <span class="contact__rule"></span>
      <span class="contact__icons">
        <span class="contact__icon">
          <svg width="13" height="13" viewBox="0 0 24 24" aria-label="Phone"><path fill="#fff" d="M6.6 10.8c1.4 2.8 3.8 5.1 6.6 6.6l2.2-2.2c.3-.3.7-.4 1-.2 1.1.4 2.3.6 3.6.6.6 0 1 .4 1 1V20c0 .6-.4 1-1 1C10.6 21 3 13.4 3 4c0-.6.4-1 1-1h3.5c.6 0 1 .4 1 1 0 1.3.2 2.5.6 3.6.1.3 0 .7-.2 1l-2.3 2.2z"/></svg>
        </span>
        <span class="contact__icon">
          <svg width="13" height="13" viewBox="0 0 24 24" aria-label="Email"><path fill="#fff" d="M3 5h18v14H3z"/><path fill="none" stroke="#1aa39b" stroke-width="1.8" d="M3 6l9 7 9-7"/></svg>
        </span>
        <span class="contact__icon">
          <svg width="14" height="14" viewBox="0 0 24 24" aria-label="Website"><circle cx="12" cy="12" r="9" fill="none" stroke="#fff" stroke-width="2"/><ellipse cx="12" cy="12" rx="4" ry="9" fill="none" stroke="#fff" stroke-width="1.6"/><path d="M3 12h18" stroke="#fff" stroke-width="1.6"/></svg>
        </span>
      </span>
      <span class="contact__rule"></span>
    </div>
    <p class="contact__details">555-201-7486<br>hello@gentlerest.com<br>GentleRest.com</p>
  </section>

  <section class="card card--brand">
    <p class="brand__name">gentlerest.com</p>
  </section>
</body>
</html>
```